Home Services (heating, cooling, electrical, plumbing) postcard design

We are looking for postcards to way to send a brief written message to our clients. Most often these will be used by the sales team but there will be opportunity for our techs to reach out to their clients as well.
We don't want them to be sales-y so if the logo, name, or taglines are used we prefer it to be more subtle.
It also doesn't need to match our website design as we are looking for a more casual feel. Something nostalgic/retro/vintage might be fun.

About us: (PLEASE DO NOT USE ANY OF THE FOLLOWING PHRASING ON THE DESIGN, this information is just to give you an idea of who we are)
- a service company that focuses on heating, cooling, electrical and plumbing service and retrofit (residential and commercial)
- family owned
- based in Warman which is a smaller city in rural Saskatchewan
- we have used the tagline "ensuring your comfort, safety and health since 2009"
- values: gratitude, stewardship, teamwork, lifelong learning, communication, quality, service
- we are professional but not stuffy, we have a fun team
- we like to inform and educate our clients

Target Market(s)

clients that we have already engaged with, we are often reaching out to say thanks (for referrals, or for the opportunity to serve them)

Industry/Entity Type

HVAC (heating, ventilation, ac), electrical, plumbing

Requirements
Must have
• Enough room on the back of postcard for mailing address and larger blank space for a message.
Nice to have
• Original designs or artwork (try to avoid stock photos), vintage feel
Should not have
• prefer not to be sales-y or promotional, it's not meant to be about us, any use of BrindleVox logo or information should be subtle

```html
<!DOCTYPE html>
<html lang="en">
<head>
<meta charset="utf-8">
<title>BrindleVox Postcard – Front and Back</title>
<link rel="stylesheet" href="https://fonts.googleapis.com/css2?family=Libre+Caslon+Text:wght@400;700&family=Roboto:wght@500;700&display=swap">
<style>
  :root {
    --backdrop: #7a7a7a;
    --orange: #e2622a;
    --orange-deep: #c9501f;
    --city-dark: #9c3f1c;
    --ribbon: #efefef;
    --ribbon-fold: #d8d6c8;
    --ink: #444444;
    --cream: #fdf9f1;
    --white: #ffffff;
    --rule: #8a8a8a;
    --logo-ink: #2d6db4;
  }
  * { margin: 0; padding: 0; box-sizing: border-box; }
  html, body { width: 1200px; height: 1200px; overflow: hidden; }
  body {
    background: var(--backdrop);
    position: relative;
    font-family: "Libre Caslon Text", Georgia, serif;
  }
  .postcard {
    position: absolute;
    left: 254px;
    width: 691px;
    height: 470px;
    background: var(--white);
    overflow: hidden;
  }
  .postcard--front { top: 92px; }
  .postcard--back { top: 628px; }

  .orange-field {
    position: absolute;
    left: 0; top: 0;
    width: 691px; height: 359px;
    background: radial-gradient(ellipse at 50% 40%, #e86c33 0%, var(--orange) 55%, var(--orange-deep) 100%);
  }
  .zigzag {
    position: absolute;
    left: 0; top: 359px;
    width: 691px; height: 11px;
  }

  /* Front */
  .note-line {
    position: absolute;
    left: 161px; top: 76px;
    width: 369px; height: 32px;
  }
  .note-line__text {
    position: absolute; inset: 0;
    display: flex; align-items: center; justify-content: center;
    color: var(--white);
    font-size: 19px;
    letter-spacing: 0.5px;
    white-space: nowrap;
  }
  .banner {
    position: absolute;
    left: 66px; top: 121px;
    width: 559px; height: 69px;
  }
  .banner__text {
    position: absolute;
    left: 47px; top: 0; width: 465px; height: 55px;
    display: flex; align-items: center; justify-content: center;
    color: var(--ink);
    font-size: 36px;
    letter-spacing: 0.5px;
    white-space: nowrap;
  }
  .sign-off {
    position: absolute;
    left: 0; top: 184px; width: 691px;
    display: flex; align-items: center; justify-content: center; gap: 12px;
    color: var(--white);
    font-size: 17px;
    white-space: nowrap;
  }
  .sign-off::before, .sign-off::after {
    content: ""; width: 22px; height: 1.5px; background: var(--white);
  }
  .city-view {
    position: absolute;
    left: 0; top: 230px;
    width: 691px; height: 129px;
    background: linear-gradient(180deg, rgba(156,63,28,0) 0%, rgba(156,63,28,0.45) 40%, rgba(156,63,28,0.6) 75%, rgba(201,80,31,0.4) 100%);
  }
  .brand {
    position: absolute;
    left: 0; width: 691px;
    display: flex; flex-direction: column; align-items: center;
  }
  .postcard--front .brand { top: 390px; }
  .brand__name {
    display: flex; align-items: center; gap: 7px;
    color: var(--logo-ink);
    font-family: "Roboto", Arial, sans-serif;
    font-weight: 700;
    font-size: 26px;
    line-height: 1;
  }
  .brand__dot {
    width: 16px; height: 16px; border-radius: 50%;
    background: var(--orange);
  }
  .brand__services {
    margin-top: 8px;
    font-family: "Roboto", Arial, sans-serif;
    font-weight: 500;
    font-size: 9.5px;
    color: #222;
    white-space: nowrap;
  }

  /* Back */
  .visit {
    position: absolute;
    left: 67px; top: 66px; width: 221px;
    text-align: center;
    color: var(--white);
    font-weight: 700;
    font-size: 14.5px;
  }
  .web-address {
    position: absolute;
    left: 67px; top: 91px;
    width: 221px; height: 23px;
    background: var(--white);
    display: flex; align-items: center; justify-content: center;
    font-family: "Roboto", Arial, sans-serif;
    font-size: 11px;
    letter-spacing: 2.6px;
    color: #333;
    white-space: nowrap;
  }
  .plumber-scene {
    position: absolute;
    left: 0; top: 150px;
    width: 346px; height: 209px;
    background: linear-gradient(180deg, rgba(156,63,28,0) 0%, rgba(156,63,28,0.25) 55%, rgba(120,50,25,0.4) 100%);
  }
  .side-strip {
    position: absolute;
    left: 664px; top: 170px;
    width: 27px; height: 189px;
    background: linear-gradient(180deg, rgba(156,63,28,0.15), rgba(156,63,28,0.5));
  }
  .postcard--back .brand {
    left: 65px; width: 200px; top: 397px;
  }
  .postcard--back .brand__name { font-size: 17px; gap: 5px; }
  .postcard--back .brand__dot { width: 11px; height: 11px; }
  .postcard--back .brand__services { margin-top: 6px; font-size: 6.5px; }

  .message-panel {
    position: absolute;
    left: 346px; top: 28px;
    width: 318px; height: 413px;
    background: var(--cream);
  }
  .stamp-box {
    position: absolute;
    left: 224px; top: 30px;
    width: 69px; height: 82px;
    border: 1px solid #666;
  }
  .address-line {
    position: absolute;
    left: 34px; width: 259px; height: 1px;
    background: var(--rule);
  }
  .address-line--one { top: 174px; }
  .address-line--two { top: 254px; }
</style>
</head>
<body>

<section class="postcard postcard--front">
  <div class="orange-field"></div>
  <div class="city-view" role="img" aria-label="Photograph of a city skyline and an empty road, tinted orange"></div>

  <div class="note-line">
    <svg width="369" height="32" viewBox="0 0 369 32" aria-hidden="true">
      <polygon points="1,1 368,1 358,16 368,31 1,31 11,16" fill="none" stroke="#ffffff" stroke-width="1" stroke-dasharray="1.5 2"/>
    </svg>
    <div class="note-line__text">A FRIENDLY NOTE TO SAY</div>
  </div>

  <div class="banner">
    <svg width="559" height="69" viewBox="0 0 559 69" aria-hidden="true">
      <polygon points="0,13 47,13 47,55 66,69 0,69 22,41" fill="var(--ribbon)"/>
      <polygon points="559,13 512,13 512,55 493,69 559,69 537,41" fill="var(--ribbon)"/>
      <polygon points="47,55 66,55 66,69" fill="var(--ribbon-fold)"/>
      <polygon points="512,55 493,55 493,69" fill="var(--ribbon-fold)"/>
      <rect x="47" y="0" width="465" height="55" fill="var(--ribbon)"/>
    </svg>
    <div class="banner__text">THANK YOU KINDLY</div>
  </div>

  <div class="sign-off">FROM OUR CREW</div>

  <svg class="zigzag" viewBox="0 0 691 11" preserveAspectRatio="none" aria-hidden="true">
    <defs>
      <pattern id="teeth-front" width="18.2" height="11" patternUnits="userSpaceOnUse">
        <polygon points="0,0 18.2,0 9.1,11" fill="var(--orange-deep)"/>
      </pattern>
    </defs>
    <rect width="691" height="11" fill="url(#teeth-front)"/>
  </svg>

  <div class="brand">
    <div class="brand__name"><span class="brand__dot"></span>BrindleVox</div>
    <div class="brand__services">Heating • Cooling • Electrical • Plumbing</div>
  </div>
</section>

<section class="postcard postcard--back">
  <div class="orange-field"></div>
  <div class="side-strip" role="img" aria-label="Edge of the orange-tinted city photograph"></div>

  <div class="visit">Visit for more info</div>
  <div class="web-address">www.websitename.com</div>

  <div class="plumber-scene" role="img" aria-label="Illustration of a plumber holding a wrench beside pipes, valves and a toolbox"></div>

  <svg class="zigzag" viewBox="0 0 691 11" preserveAspectRatio="none" aria-hidden="true">
    <defs>
      <pattern id="teeth-back" width="18.2" height="11" patternUnits="userSpaceOnUse">
        <polygon points="0,0 18.2,0 9.1,11" fill="var(--orange-deep)"/>
      </pattern>
    </defs>
    <rect width="691" height="11" fill="url(#teeth-back)"/>
  </svg>

  <div class="brand">
    <div class="brand__name"><span class="brand__dot"></span>BrindleVox</div>
    <div class="brand__services">Heating • Cooling • Electrical • Plumbing</div>
  </div>

  <div class="message-panel">
    <div class="stamp-box"></div>
    <div class="address-line address-line--one"></div>
    <div class="address-line address-line--two"></div>
  </div>
</section>

</body>
</html>
```